Ridgeline Build Network Inc. Letterhead

Creation of attractive and eye catching letterhead for a business start-up for the construction industry. Letterhead must relate to construction, but avoid standard hammer and tools in the design.
Updates

I forgot to add some details, sorry about that. Some pertinent info: Ph: 720-555-0148 ridgelinebuildnet.example 487 Willowmere Ave, Ste 210 Cedarbrook, CA 95699 info@ridgelinebuildnet.example not sure if slogan should be in there" “Bringing building trades together to shape a stronger, more purposeful field.” must be able to be used in word. Thanks!

```html
<!DOCTYPE html>
<html lang="en">
<head>
<meta charset="utf-8">
<title>Ridgeline Build Network Inc. Letterhead</title>
<link rel="stylesheet" href="https://fonts.googleapis.com/css2?family=Montserrat:wght@600;700&family=Roboto:wght@400&family=Great+Vibes&display=swap">
<style>
  :root {
    --navy: #1f2052;
    --red: #b8191f;
    --ink: #222222;
    --paper: #ffffff;
  }
  html, body { margin: 0; padding: 0; overflow: hidden; background: var(--paper); }
  .letterhead {
    position: relative;
    width: 927px;
    height: 1200px;
    overflow: hidden;
    background: var(--paper);
    font-family: "Roboto", Arial, sans-serif;
    color: var(--ink);
  }
  .brand {
    position: absolute;
    left: 84px;
    top: 136px;
    display: flex;
    align-items: center;
    gap: 9px;
  }
  .brand-mark { width: 14px; height: 14px; background: var(--red); }
  .brand-name {
    font-family: "Montserrat", Arial, sans-serif;
    font-weight: 700;
    font-size: 17px;
    letter-spacing: 1px;
    color: var(--navy);
    text-transform: uppercase;
  }
  .contact {
    position: absolute;
    left: 652px;
    top: 67px;
    height: 91px;
    border-left: 2px solid var(--navy);
    padding-left: 12px;
    font-family: "Montserrat", Arial, sans-serif;
    font-weight: 700;
    font-size: 11px;
    color: var(--navy);
  }
  .contact-row { display: flex; align-items: flex-start; gap: 6px; line-height: 18px; }
  .contact-row svg { width: 11px; height: 11px; margin-top: 3px; flex: none; fill: var(--red); }
  .contact-row svg.outline { fill: none; stroke: var(--red); stroke-width: 3; }
  .body-text {
    position: absolute;
    left: 85px;
    top: 268px;
    width: 780px;
    font-size: 13.6px;
    line-height: 24.6px;
  }
  .body-text p { margin: 0; }
  .date { margin-bottom: 25px !important; }
  .recipient { margin-bottom: 49px !important; }
  .salutation { margin-bottom: 24px !important; }
  .paragraph { margin-bottom: 25px !important; white-space: nowrap; }
  .signature {
    font-family: "Great Vibes", cursive;
    font-size: 40px;
    line-height: 46px;
    margin: 8px 0 2px !important;
    color: #111;
  }
  .slogan {
    position: absolute;
    left: 132px;
    top: 1113px;
    font-family: "Montserrat", Arial, sans-serif;
    font-weight: 700;
    font-size: 13.2px;
    color: var(--red);
  }
  .footer-band {
    position: absolute;
    left: 28px;
    right: 28px;
    top: 1143px;
    height: 41px;
    background: var(--navy);
  }
  .footer-url {
    position: absolute;
    left: 250px;
    top: 1155px;
    font-family: "Montserrat", Arial, sans-serif;
    font-weight: 700;
    font-size: 14.5px;
    color: var(--paper);
    letter-spacing: 0.3px;
  }
</style>
</head>
<body>
<div class="letterhead">
  <div class="brand">
    <span class="brand-mark"></span>
    <span class="brand-name">Ridgeline Build Network</span>
  </div>

  <div class="contact">
    <div class="contact-row">
      <svg viewBox="0 0 24 24"><path d="M6.6 10.8a15.1 15.1 0 0 0 6.6 6.6l2.2-2.2c.3-.3.7-.4 1-.2 1.1.4 2.3.6 3.6.6.6 0 1 .4 1 1V20c0 .6-.4 1-1 1A17 17 0 0 1 3 4c0-.6.4-1 1-1h3.5c.6 0 1 .4 1 1 0 1.3.2 2.5.6 3.6.1.3 0 .7-.2 1z"/></svg>
      <span>720-555-0148</span>
    </div>
    <div class="contact-row">
      <svg class="outline" viewBox="0 0 24 24"><path d="M2 5h20v14H2z M2 5l10 8 10-8"/></svg>
      <span>info@ridgelinebuildnet.example</span>
    </div>
    <div class="contact-row">
      <svg class="outline" viewBox="0 0 24 24"><circle cx="12" cy="12" r="9"/><path d="M3 12h18M12 3c3 3 3 15 0 18M12 3c-3 3-3 15 0 18"/></svg>
      <span>www.ridgelinebuildnet.example</span>
    </div>
    <div class="contact-row">
      <svg viewBox="0 0 24 24"><path d="M12 2a7 7 0 0 0-7 7c0 5.3 7 13 7 13s7-7.7 7-13a7 7 0 0 0-7-7zm0 9.5a2.5 2.5 0 1 1 0-5 2.5 2.5 0 0 1 0 5z"/></svg>
      <span>487 Willowmere Ave, Ste 210<br>Cedarbrook, CA 95699</span>
    </div>
  </div>

  <div class="body-text">
    <p class="date">October 22, 2018</p>
    <p class="recipient">Mr. John Doe<br>123 Main Street SW<br>Dallas, TX 75229</p>
    <p class="salutation">Dear Mr. Doe,</p>
    <p class="paragraph">Lorem ipsum dolor sit amet, consectetur adipiscing elit. Sed placerat ut nibh sed auctor. Ut risus velit, feugiat et lacinia<br>porttitor, viverra id ex. Pellentesque efficitur augue a mi egestas tempus. Duis pulvinar malesuada neque ac commodo.<br>Fusce maximus quis mi non imperdiet. Vivamus vel ornare quam. Vestibulum vitae lectus ut quam pulvinar cursus. Cras<br>vehicula ac ante vel fringilla. Maecenas placerat dictum aliquet. Nulla in odio vitae ligula feugiat tincidunt non ut lectus.</p>
    <p class="paragraph">Praesent hendrerit ac sapien in pulvinar. Vestibulum tincidunt auctor quam a hendrerit. Aenean eget molestie dui, id<br>molestie nulla. Fusce sagittis lobortis elit quis facilisis. Donec augue felis, malesuada eu imperdiet vel, tincidunt et augue.<br>Aliquam erat volutpat. Aenean suscipit metus id arcu blandit, id imperdiet arcu aliquam. In faucibus velit sit amet ex Fusce<br>gravida, odio honcus quis sagittis venenatis, mi nibh placerat dui, non mattis tellus turpis fusce ultrices massa suscipit.</p>
    <p class="paragraph">Aliquam suscipit fermentum viverra. Nam quis mi eget ex rhoncus suscipit sed in velit. Donec nec mollis purus. Nam<br>maximus ligula volutpat vulputate pulvinar. Maecenas vel sem odio. Nunc lectus augue, facilisis vitae dolor eu, aliquet<br>consequat urna. Cras congue rhoncus congue. Etiam imperdiet leo id cursus dignissim. Aenean sollicitudin magna dolor,<br>Nullam lacinia quam et mi commodo dapibus. Aenean vel quam nisl. Sed pretium augue lorem consequat felis congue ut.</p>
    <p class="closing">Regards,</p>
    <p class="signature">Signature</p>
    <p class="signer">Your Name<br>Title</p>
  </div>

  <div class="slogan">Bringing building trades together to shape a stronger, more purposeful field.</div>
  <div class="footer-band"></div>
  <div class="footer-url">www.RIDGELINEBUILDNET.example</div>
</div>
</body>
</html>
```